2 page flyer outlining details of a product framework

We need a flyer for a management consulting firm outlining a product we offer. The draft wording and company logo are attached. Logo colours should be used (Purple - C73, M93, Y0, K0 & Green - C50, M0, Y99, K0).
The look and feel should communicate a dynamic, trustworthy, credible organisation with excellence in delivery.

File must be provided in AI format to enable text changes.

Target Market(s)

Senior Business Excecutives

Industry/Entity Type

Management Consulting

Font styles to use
Other font styles liked:
• Aller & Myriad Pro

Colors
acd036
6b449b

Requirements
Must have
• Logo & wording provided, professional images and a flyer layout with space and a section for contact details.

```html
<!DOCTYPE html>
<html lang="en">
<head>
<meta charset="utf-8">
<title>FLOW! Framework Assessment – Flyer</title>
<link href="https://fonts.googleapis.com/css2?family=PT+Sans:ital,wght@0,400;0,700;1,400;1,700&family=Lilita+One&display=swap" rel="stylesheet">
<style>
:root{
  --purple:#6b449b;
  --purple-dark:#55347f;
  --green:#acd036;
  --green-deep:#8cc63f;
  --grey:#5f5f60;
  --grey-dark:#4e4e4f;
  --ink:#3a3a3a;
  --white:#ffffff;
  --backdrop:#ece9e4;
}
*{box-sizing:border-box;margin:0;padding:0}
html,body{width:1200px;height:911px;overflow:hidden}
body{background:var(--backdrop);font-family:"PT Sans",Arial,sans-serif;color:var(--ink);position:relative}
.page{position:absolute;background:var(--white);box-shadow:0 3px 10px rgba(0,0,0,.25);overflow:hidden}

/* ---------- Page one ---------- */
.page-front{left:68px;top:28px;width:534px;height:742px}
.hero-photo{position:absolute;left:0;top:0;width:250px;height:248px;background:linear-gradient(160deg,#f4f4f4 0%,#d9d5d2 45%,#3b3b40 100%)}
.brand-tile{position:absolute;left:7px;top:176px;width:80px;height:68px;background:var(--white);display:flex;align-items:center;justify-content:center;gap:4px;flex-direction:column}
.brand-dot{width:18px;height:18px;border-radius:50%;background:var(--purple)}
.brand-name{font-weight:700;color:var(--purple);font-size:8.5px;line-height:1.05;text-align:center}
.front-title{position:absolute;left:262px;top:52px;width:260px;color:var(--purple);font-weight:700;font-style:italic;font-size:15px;line-height:1.3;text-transform:uppercase}
.dotted-rule{position:absolute;left:262px;top:97px;width:250px;border-top:2px dotted var(--purple)}
.front-questions{position:absolute;left:262px;top:112px;width:262px;font-size:13.3px;line-height:1.3;color:var(--ink)}
.front-questions p{margin-bottom:9px}
.intro-band{position:absolute;left:0;top:250px;width:534px;height:88px;background:linear-gradient(90deg,var(--purple-dark),var(--purple));color:var(--white);font-style:italic;font-weight:700;font-size:12.2px;line-height:1.35;padding:11px 14px}
.areas-band{position:absolute;left:0;top:342px;width:534px;height:24px;background:var(--green-deep);color:var(--white);font-weight:700;font-size:12.2px;text-align:center;line-height:24px;text-transform:uppercase}
.area{position:absolute;width:240px}
.area-num{position:absolute;left:0;top:-10px;font-size:86px;font-weight:700;color:var(--green-deep);line-height:1}
.area-body{margin-left:50px}
.area h3{color:var(--green-deep);font-size:12.5px;font-weight:700;text-transform:uppercase;line-height:1.15}
.area h4{font-size:9.6px;font-style:italic;font-weight:700;color:var(--ink);line-height:1.25;margin-bottom:6px}
.area p,.area li{font-size:7.6px;line-height:1.3;color:var(--ink)}
.area ul{list-style:none;margin-left:10px}
.area li::before{content:"• "}
.area-1{left:26px;top:384px}
.area-2{left:268px;top:384px}
.area-3{left:26px;top:512px}
.area-4{left:268px;top:512px}
.contact-footer{position:absolute;left:0;bottom:0;width:100%;height:72px;background:var(--grey);color:var(--white);font-size:7.8px;line-height:1.3;padding:20px 30px}
.footer-brand{position:absolute;right:22px;top:20px;display:flex;align-items:center;gap:4px;font-weight:700;font-size:9px;color:var(--white)}
.footer-brand .brand-dot{background:var(--white);width:13px;height:13px}

/* ---------- Page two ---------- */
.page-back{left:612px;top:118px;width:563px;height:722px}
.phase-column{position:absolute;left:0;top:0;width:191px;height:662px;background:var(--green-deep)}
.phase-intro{margin:0 10px;padding:30px 0 8px;color:var(--white);font-weight:700;font-size:10.6px;text-transform:uppercase;line-height:1.25;text-align:center;border-bottom:2px dotted var(--white)}
.phase-title{color:var(--white);font-weight:700;font-size:13.3px;margin:10px 0 6px 8px}
.phase-title em{font-weight:700}
.phase-list{list-style:none;padding:0 6px 0 9px}
.phase-list li{color:var(--purple-dark);font-style:italic;font-weight:700;font-size:10.6px;line-height:1.53;padding-left:6px;text-indent:-6px}
.phase-list li::before{content:"·"}
.info-column{position:absolute;left:191px;top:0;width:372px;height:662px;background:var(--grey)}
.info-heading{padding:14px 10px 0;color:var(--white);font-weight:700;font-style:italic;font-size:15.6px;line-height:1.2;text-transform:uppercase}
.info-lead{position:absolute;left:0;top:102px;width:372px;height:98px;background:var(--purple);color:var(--white);font-weight:700;font-style:italic;font-size:11.6px;line-height:1.3;padding:8px 10px}
.logo-panel{position:absolute;left:0;top:200px;width:372px;height:152px;background:var(--white);display:flex;align-items:center;justify-content:center;gap:10px}
.logo-panel .brand-dot{width:40px;height:40px}
.logo-panel .brand-name{font-size:26px;text-align:left;line-height:1.05}
.price-band{position:absolute;left:0;top:357px;width:372px;height:48px;background:var(--purple);color:var(--white);font-family:"Lilita One","PT Sans",sans-serif;font-size:19px;text-align:center;line-height:48px}
.call-box{position:absolute;left:0;top:412px;width:372px;height:98px;display:flex;align-items:center;padding:0 14px;gap:10px}
.call-box svg{flex:none}
.call-text{color:var(--white);font-weight:700;font-style:italic;font-size:14.8px;line-height:1.3;text-align:center;flex:1}
.discount-band{position:absolute;left:0;top:515px;width:372px;height:58px;background:var(--purple);color:var(--green);font-family:"Lilita One","PT Sans",sans-serif;font-size:17px;text-align:center;line-height:1.25;padding-top:8px}
.fine-print{position:absolute;left:0;top:578px;width:372px;height:84px;background:var(--green-deep);color:var(--ink);font-size:6.8px;line-height:1.3;padding:6px 12px}
.back-footer{position:absolute;left:0;top:662px;width:563px;height:60px;background:var(--grey);color:var(--white);font-size:7.8px;line-height:1.3;padding:12px 30px}
.back-footer .footer-brand{top:20px}
</style>
</head>
<body>

<section class="page page-front">
  <div class="hero-photo" role="img" aria-label="Photograph of a smiling business team in suits, standing together"></div>
  <div class="brand-tile"><span class="brand-dot"></span><span class="brand-name">Meridian Management Consulting</span></div>

  <h1 class="front-title">Focused Lean Optimised Workforce (FLOW!) Framework Assessment</h1>
  <div class="dotted-rule"></div>
  <div class="front-questions">
    <p>How much is inefficient workforce management costing your business?</p>
    <p>Are you as efficient as you could be?</p>
    <p>Find the answers with a powerful Focused Lean Optimised Workforce ™ (FLOW!) Framework Assessment!</p>
  </div>

  <div class="intro-band">We provide a detailed, tailored assessment based on our proprietary FLOW! Framework. Our framework is scalable and flexible to suit organisations of any size and structure – providing you with a roadmap to successfully achieving better business outcomes, greater efficiency, and cost savings.</div>
  <div class="areas-band">Our FLOW! Framework assessment looks at the following key areas</div>

  <article class="area area-1">
    <span class="area-num">1</span>
    <div class="area-body">
      <h3>Planning Capability</h3>
      <h4>How well do you predict and plan for the future?</h4>
      <p>We review how you approach forecasting and scheduling activities, including:</p>
      <ul><li>Data accuracy and validity</li><li>Known variations (i.e. Public Holidays &amp; Marketing activities)</li><li>Assumptions used in the planning process</li></ul>
    </div>
  </article>
  <article class="area area-2">
    <span class="area-num">2</span>
    <div class="area-body">
      <h3>Real Time Management</h3>
      <h4>How well do you respond to changing needs and unexpected events?</h4>
      <p>We review how you manage intraday activities, including:</p>
      <ul><li>Reforecasting and planning</li><li>Managing exceptions</li><li>Recovery strategies</li></ul>
    </div>
  </article>
  <article class="area area-3">
    <span class="area-num">3</span>
    <div class="area-body">
      <h3>System Interaction and Acceptance</h3>
      <h4>How well have you enabled and empowered your team to get the most out of the system?</h4>
      <p>We review how you utilise and enable capabilities such as:</p>
      <ul><li>Use of self-service functionality</li><li>Use of meeting and training scheduling functionality</li><li>Support team autonomy and interaction with the system</li></ul>
    </div>
  </article>
  <article class="area area-4">
    <span class="area-num">4</span>
    <div class="area-body">
      <h3>Reporting</h3>
      <h4>How well are you using the valuable data available to make informed business decisions?</h4>
      <p>We review how you utilise available reports and data, including:</p>
      <ul><li>Information currently reported</li><li>Inclusion of workforce management metrics in management reports</li><li>Accuracy and validity of reported metrics</li></ul>
    </div>
  </article>

  <footer class="contact-footer">
    Your company address here.<br>Phone: 555-555-555 | Fax: 555-555-555<br>Email: email@yourcompany.com
    <div class="footer-brand"><span class="brand-dot"></span>Meridian</div>
  </footer>
</section>

<section class="page page-back">
  <div class="phase-column">
    <div class="phase-intro">A typical FLOW! Framework assessment is structured over a number of phases</div>
    <h2 class="phase-title">PHASE 1 | <em>Analysis</em></h2>
    <ul class="phase-list">
      <li>Survey designed and distributed</li>
      <li>Initial briefing with Contact Centre Manager</li>
      <li>Detailed overview of workforce management system and processes with Workforce Management team members</li>
      <li>Interviews with Team Leaders</li>
      <li>Interviews with Quality Assurance team members</li>
      <li>Interviews with Training team members</li>
      <li>Interviews with frontline staff</li>
      <li>Follow up discussions with Workforce Management team members as required</li>
    </ul>
    <h2 class="phase-title">PHASE 2 | Report Development</h2>
    <ul class="phase-list">
      <li>Development of initial report of findings</li>
      <li>Discussions with solution vendor (where available) to confirm system capability in addressing key problem areas identified</li>
      <li>Development of final report including recommendations for enhancement</li>
    </ul>
    <h2 class="phase-title">PHASE 3 | Report Delivery</h2>
    <ul class="phase-list">
      <li>Delivery of final report including observations and key recommendations</li>
    </ul>
  </div>

  <div class="info-column">
    <h2 class="info-heading">You may be wondering what is involved in the FLOW! Framework assessment?</h2>
    <p class="info-lead">To keep your team hard at work doing what they do best, we conduct our FLOW! Framework Assessment in just a few interviews over a 2-day site visit. For larger and multi-site organisations we also use online surveys to increase the amount of data we can capture with minimal business disruption.</p>
    <div class="logo-panel"><span class="brand-dot"></span><span class="brand-name">Meridian<br>Management Consulting</span></div>
    <div class="price-band">FULL PACKAGE PRICE $10,000 (EX GST)</div>
    <div class="call-box">
      <svg width="56" height="60" viewBox="0 0 56 60" aria-hidden="true">
        <path d="M10 6c3-2 6-2 8 1l5 9c1 3 0 5-2 6l-3 2c2 6 7 12 13 15l2-3c2-2 4-2 6-1l8 6c2 2 2 5 0 7l-4 4c-4 3-12 1-20-6S4 28 5 17c0-4 2-8 5-11z" fill="var(--white)"/>
        <path d="M32 14a12 12 0 0 1 10 10M32 6a20 20 0 0 1 18 18M32 22a5 5 0 0 1 3 3" stroke="var(--white)" stroke-width="3" fill="none" stroke-linecap="round"/>
      </svg>
      <p class="call-text">Call<br>Meridian Management Consulting<br>To Book In For Your Assessment Today!</p>
    </div>
    <div class="discount-band">25% DISCOUNT<br>FOR KEY CUSTOMERS $7,500 (EX GST)</div>
    <div class="fine-print">
      -Discount offer valid until 30th June 2015, unless sold out prior.<br>
      -FLOW! Framework Assessment structure is indicative and may vary for each organisation<br>
      -Package price includes 2 days on site plus report preparation, which is suitable for a small to medium sized contact centre with a centralised workforce management team. Larger clients or those with decentralised workforce management teams may request extra on-site days for an additional fee.
    </div>
  </div>

  <footer class="back-footer">
    Your company address here.<br>Phone: 555-555-555 | Fax: 555-555-555<br>Email: email@yourcompany.com
    <div class="footer-brand"><span class="brand-dot"></span>Meridian</div>
  </footer>
</section>

</body>
</html>
```